Plakate für ein Fest
Zielgruppe
Das Lindtal Hof ist ein Gewerbepark mit unterschiedlichen Mietern von Handwerker über Musiker bis hin zu Vermögensberatung. Wir veranstalten ein Fest für unsere Mieter und möchten dieses Plakat als Einladung nutzen.
Aufgabenstellung
Hintergrund schwarz, Logo verwenden
Get together
BBQ & Cocktails im Lindtal Hof
am 13.10.2023 ab 18 Uhr
Logo Band brisk notes
Kinderbereich
Wir freuen uns darauf, alle Mieter mit Familien begrüßen zu dürfen! Auch an die Kleinen haben wir gedacht.

```html
<!DOCTYPE html>
<html lang="de">
<head>
<meta charset="utf-8">
<title>Get together – BBQ &amp; Cocktails im Lindtal Hof</title>
<link rel="stylesheet" href="https://fonts.googleapis.com/css2?family=Quicksand:wght@400;500;700&display=swap">
<style>
  :root {
    --bg: #000000;
    --text: #ffffff;
    --fire-core: #ffb020;
    --fire-mid: #e2561a;
    --fire-dark: #5a1606;
    --ember: #7a2a0c;
    --logo-box: #1b1b1b;
    --logo-accent: #3cb44a;
  }
  * { margin: 0; padding: 0; box-sizing: border-box; }
  html, body {
    width: 900px;
    height: 1200px;
    overflow: hidden;
    background: var(--bg);
  }
  .poster {
    position: relative;
    width: 900px;
    height: 1200px;
    background: var(--bg);
    color: var(--text);
    font-family: "Quicksand", sans-serif;
    overflow: hidden;
  }
  .headline-art {
    position: absolute;
    left: 130px;
    top: 35px;
    width: 675px;
    height: 335px;
    border-radius: 40px;
    background: radial-gradient(ellipse at 50% 50%, var(--fire-core) 0%, var(--fire-mid) 38%, var(--fire-dark) 68%, rgba(0,0,0,0) 85%);
    opacity: 0.85;
  }
  .food-scene {
    position: absolute;
    left: 0;
    top: 720px;
    width: 900px;
    height: 480px;
    background:
      radial-gradient(ellipse at 18% 55%, rgba(70,90,170,0.55) 0%, rgba(0,0,0,0) 40%),
      radial-gradient(ellipse at 72% 70%, rgba(120,55,25,0.85) 0%, rgba(0,0,0,0) 50%),
      linear-gradient(to bottom, rgba(0,0,0,0) 0%, var(--ember) 78%, var(--fire-mid) 100%);
  }
  .text-block {
    position: absolute;
    left: 0;
    width: 900px;
    text-align: center;
    white-space: nowrap;
  }
  .title-kicker { top: 325px; left: 444px; width: auto; transform: translateX(-50%); font-size: 55px; font-weight: 400; }
  .title-main { top: 400px; left: 443px; width: auto; transform: translateX(-50%); font-size: 61px; font-weight: 400; }
  .title-date { top: 483px; left: 472px; width: auto; transform: translateX(-50%); font-size: 67px; font-weight: 400; }
  .invite {
    top: 580px;
    left: 468px;
    width: auto;
    transform: translateX(-50%);
    font-size: 28px;
    font-weight: 500;
    line-height: 51.5px;
  }
  .band-label { top: 775px; left: 474px; width: auto; transform: translateX(-50%); font-size: 30px; font-weight: 500; }
  .band-name { top: 818px; left: 469px; width: auto; transform: translateX(-50%); font-size: 40px; font-weight: 700; letter-spacing: 1px; }
  .brand-box {
    position: absolute;
    left: 333px;
    top: 1071px;
    width: 246px;
    height: 101px;
    background: var(--logo-box);
    display: flex;
    align-items: center;
    justify-content: center;
    gap: 14px;
  }
  .brand-mark { width: 22px; height: 22px; background: var(--logo-accent); }
  .brand-name {
    font-size: 29px;
    font-weight: 700;
    line-height: 1;
    color: var(--text);
    letter-spacing: 1px;
  }
</style>
</head>
<body>
  <main class="poster">
    <div class="headline-art" role="img" aria-label="Flammender Schriftzug BBQ"></div>
    <div class="food-scene" role="img" aria-label="Bunte Cocktails mit Eis und Beeren neben Steaks auf dem Grill über Flammen"></div>

    <p class="text-block title-kicker">Get together</p>
    <h1 class="text-block title-main">BBQ &amp; Cocktails im Lindtal Hof</h1>
    <p class="text-block title-date">am 13.10.2023 ab 18 Uhr</p>

    <p class="text-block invite">Wir freuen uns darauf,<br>alle Mieter mit Familien begrüßen zu dürfen!<br>Auch an die Kleinen haben wir gedacht.</p>

    <p class="text-block band-label">Funk &amp; Soulband</p>
    <p class="text-block band-name">brisk notes</p>

    <div class="brand-box">
      <span class="brand-mark"></span>
      <span class="brand-name">LINDTAL HOF</span>
    </div>
  </main>
</body>
</html>
```